CD Cover Art for our German Song "Beneath the Willow Bright"

CD Cover Art for my Band LanternPair

To be used for all main online streaming services (Tunevault, Pear Sounds, Wubble, etc.)

German Song Title: "Beneath the Willow Bright" <> engl .: Beneath the Willow Bright

THE IDEA:
The artwork is to evoke a feeling of happiness in spring. It needs to be visually striking and shining.

For some inspiration you can already hear the song in a live video here (I'm the crazy drummer):
https://www.snapgridly.example/p/XQr7-tLpZvw/

We want you to include ...
- flowers blooming in a meadow, with a small blue stream running through the picture.
- the band logo LanternPair in the bottom right corner.
- the song title "Beneath the willow bright"

It would be awesome to see a bright female silouhette standing on the meadow with outstretched arms (pointing to the sky) and letting the sunlight shine on her.

----------------
A lyrics snippet:

First verse:
One morning I woke up
Felt myself being watched
You looked at me and laughed
You had drawn something on the window

To draw my attention outside
Trying to show me what I usually miss
The beautiful flowers and meadows
It's about time I understood

Chorus:
Beneath the willow bright, there everything blossoms
No matter how long it takes
Beneath the willow bright, we never give up
Everything takes its course

https://www.lanternpair-tunes.example

Thank you very much to all of you amazing designers and for your proposals and great work!
It was really a pleasure to see all the creativity you put on our project.
All the best!
LanternPair

Target Market(s)

Industry/Entity Type

Music Download

Font styles to use
Sans Serif

Requirements
Must have
• The artwork is to evoke a feeling of happiness in spring. It needs to be visually striking and shining.

Nice to have
• It would be awesome to see a bright female silouhette standing on the meadow with outstretched arms (pointing to the sky) and letting the sunlight shine on her.

```html
<!DOCTYPE html>
<html lang="en">
<head>
<meta charset="utf-8">
<title>Beneath the Willow Bright — LanternPair</title>
<link rel="stylesheet" href="https://fonts.googleapis.com/css2?family=Bebas+Neue&family=Mr+Dafoe&display=swap">
<style>
  :root {
    --backdrop: #060c52;
    --title-yellow: #fff200;
    --title-white: #ffffff;
    --sky-grey: #6f6d6b;
    --mountain-grey: #55585a;
    --lake-silver: #c9ccce;
    --meadow-gold: #9a8a4a;
    --meadow-green: #4f6b33;
    --bloom-pink: #c8245a;
    --bloom-white: #e9e6df;
  }
  * { margin: 0; padding: 0; box-sizing: border-box; }
  html, body {
    width: 1200px;
    height: 1000px;
    overflow: hidden;
    background: var(--backdrop);
  }
  .cover {
    position: absolute;
    left: 182px;
    top: 82px;
    width: 838px;
    height: 838px;
    overflow: hidden;
    box-shadow: 0 10px 30px rgba(0, 0, 0, 0.45);
  }
  .cover-scene {
    position: absolute;
    inset: 0;
    background:
      radial-gradient(ellipse 60% 30% at 85% 88%, rgba(200, 36, 90, 0.75), transparent 70%),
      radial-gradient(ellipse 55% 25% at 25% 95%, rgba(200, 36, 90, 0.6), transparent 70%),
      radial-gradient(ellipse 40% 18% at 50% 82%, rgba(233, 230, 223, 0.45), transparent 70%),
      linear-gradient(180deg,
        var(--sky-grey) 0%,
        var(--mountain-grey) 30%,
        #7a7468 46%,
        var(--lake-silver) 52%,
        #b9bcbc 60%,
        var(--meadow-gold) 67%,
        var(--meadow-green) 76%,
        #7a3a4c 88%,
        var(--bloom-pink) 100%);
  }
  .song-title {
    position: absolute;
    left: 56px;
    top: 72px;
    font-family: "Bebas Neue", "Oswald", sans-serif;
    line-height: 0.86;
  }
  .song-title__lead {
    display: block;
    color: var(--title-yellow);
    font-size: 108px;
  }
  .song-title__main {
    display: block;
    color: var(--title-white);
    font-size: 188px;
    margin-top: -4px;
  }
  .song-title__script {
    position: absolute;
    left: 52px;
    top: 255px;
    font-family: "Mr Dafoe", cursive;
    color: var(--title-yellow);
    font-size: 190px;
    line-height: 1;
    white-space: nowrap;
  }
  .band-name {
    position: absolute;
    right: 52px;
    bottom: 80px;
    display: flex;
    align-items: center;
    gap: 12px;
  }
  .band-name__dot {
    width: 30px;
    height: 30px;
    border-radius: 50%;
    background: var(--title-yellow);
  }
  .band-name__text {
    font-family: "Bebas Neue", "Oswald", sans-serif;
    font-size: 52px;
    color: var(--title-yellow);
    letter-spacing: 1px;
  }
</style>
</head>
<body>
  <main class="cover">
    <div class="cover-scene" role="img" aria-label="Photograph of a grey mountain range above a silver lake, a woman in a red dress and hat on a wooden pier, and a meadow of pink and white wildflowers in the foreground"></div>
    <h1 class="song-title">
      <span class="song-title__lead">Beneath the</span>
      <span class="song-title__main">Willow</span>
    </h1>
    <p class="song-title__script">Bright</p>
    <div class="band-name">
      <span class="band-name__dot"></span>
      <span class="band-name__text">LanternPair</span>
    </div>
  </main>
</body>
</html>
```